TARO PTY LTD - Business Cards

Design a modern business card - using the attached Designs.
Same design as on the front, apart from the names/numbers/emails to be different.
We want the cards to be very glossy to stand out, do I think the simple black/white/metallic will be effective.
Both lots of details below:

Lyle Marrick
Director
lyle_taro@quintmail.example
0493 628 304

Simon Prowle
Director
simon_taro@quintmail.example
0438 514 209

```html
<!DOCTYPE html>
<html lang="en">
<head>
<meta charset="utf-8">
<title>TARO PTY LTD – Business Cards</title>
<link rel="stylesheet" href="https://fonts.googleapis.com/css2?family=Exo+2:wght@400;600&display=swap">
<style>
  :root{
    --bg:#e9e8e6;
    --card-dark:#303337;
    --card-edge:#4a4e53;
    --silver-light:#f4f4f4;
    --silver-mid:#d2d3d5;
    --band-grey:#8e9094;
    --ink-dark:#2e3135;
    --ink-light:#ffffff;
  }
  html,body{margin:0;padding:0;}
  body{
    width:1200px;height:970px;overflow:hidden;
    background:var(--bg);
    font-family:"Exo 2",sans-serif;
  }
  .card{
    position:absolute;left:230px;width:740px;height:423px;
    box-shadow:0 10px 24px rgba(0,0,0,.25);border-radius:6px;
  }
  .card--back{top:40px;}
  .card--front{top:505px;}
  .card svg{display:block;width:740px;height:423px;}
  .brand{font-family:"Exo 2",sans-serif;font-weight:600;font-size:30px;fill:var(--ink-dark);letter-spacing:2px;}
  .web{font-size:15px;fill:var(--ink-light);}
  .address{font-size:17px;fill:var(--ink-light);letter-spacing:.5px;}
  .person-name{font-size:26px;font-weight:600;fill:var(--ink-dark);letter-spacing:1px;}
  .person-role{font-size:17px;fill:var(--ink-dark);letter-spacing:1.5px;}
  .contact{font-size:16px;fill:var(--ink-light);}
  .icon{fill:none;stroke:var(--ink-light);stroke-width:1.6;}
</style>
</head>
<body>

<!-- Back side -->
<div class="card card--back">
  <svg viewBox="0 0 740 423">
    <defs>
      <linearGradient id="silverPanel" x1="0" y1="0" x2="1" y2="1">
        <stop offset="0" stop-color="var(--silver-light)"/>
        <stop offset="1" stop-color="var(--silver-mid)"/>
      </linearGradient>
      <linearGradient id="greyBand" x1="0" y1="0" x2="1" y2="0">
        <stop offset="0" stop-color="#a7a9ac"/>
        <stop offset="1" stop-color="#6f7276"/>
      </linearGradient>
      <linearGradient id="worldMapTone" x1="0" y1="0" x2="1" y2="0">
        <stop offset="0" stop-color="#e2e3e5"/>
        <stop offset="1" stop-color="#cfd0d3"/>
      </linearGradient>
      <clipPath id="backPanelClip">
        <polygon points="30,30 545,30 495,320 420,320 405,336 390,320 30,320"/>
      </clipPath>
    </defs>
    <rect width="740" height="423" rx="6" fill="var(--card-dark)"/>
    <rect x="14" y="14" width="712" height="395" rx="3" fill="none" stroke="var(--card-edge)"/>
    <polygon points="30,30 545,30 495,320 420,320 405,336 390,320 30,320" fill="url(#silverPanel)"/>
    <g clip-path="url(#backPanelClip)">
      <rect x="30" y="30" width="515" height="290" fill="url(#worldMapTone)" opacity=".7"
            role="img" aria-label="Faint world map across the silver panel"/>
    </g>
    <polygon points="570,30 660,30 610,320 520,320" fill="url(#greyBand)"/>
    <g class="brand-mark">
      <circle cx="240" cy="175" r="9" fill="var(--ink-dark)"/>
      <text class="brand" x="258" y="186">TARO</text>
    </g>
    <text class="web" x="40" y="392">www.tarocards.example</text>
  </svg>
</div>

<!-- Front side -->
<div class="card card--front">
  <svg viewBox="0 0 740 423">
    <defs>
      <linearGradient id="silverPanelFront" x1="0" y1="0" x2="1" y2="1">
        <stop offset="0" stop-color="var(--silver-light)"/>
        <stop offset="1" stop-color="var(--silver-mid)"/>
      </linearGradient>
      <linearGradient id="nameBand" x1="0" y1="0" x2="1" y2="0">
        <stop offset="0" stop-color="#ffffff"/>
        <stop offset="1" stop-color="#c9cacc"/>
      </linearGradient>
    </defs>
    <rect width="740" height="423" rx="6" fill="var(--card-dark)"/>
    <rect x="14" y="14" width="712" height="395" rx="3" fill="none" stroke="var(--card-edge)"/>

    <polygon points="30,30 490,30 462,90 30,90" fill="var(--band-grey)"/>
    <text class="address" x="45" y="67">27 Kessel Road, Level 3, Harwick St.</text>

    <polygon points="30,102 450,102 420,172 30,172" fill="url(#nameBand)"/>
    <text class="person-name" x="45" y="134">LYLE MARRICK</text>
    <text class="person-role" x="45" y="159">DIRECTOR</text>

    <polygon points="540,30 590,30 604,44 618,30 710,30 710,393 440,393" fill="url(#silverPanelFront)"/>
    <g class="brand-mark">
      <circle cx="548" cy="212" r="9" fill="var(--ink-dark)"/>
      <text class="brand" x="566" y="223">TARO</text>
    </g>

    <g class="contacts">
      <path class="icon" d="M48 215c2 5 5 8 10 10l2-3 3 1v4c-9 0-16-7-16-16h4l1 3z"/>
      <text class="contact" x="75" y="225">0493 628 304</text>

      <rect class="icon" x="50" y="244" width="9" height="15" rx="1.5"/>
      <text class="contact" x="75" y="257">0438 514 209</text>

      <rect class="icon" x="47" y="281" width="15" height="9"/>
      <rect class="icon" x="50" y="276" width="9" height="5"/>
      <text class="contact" x="75" y="289">0493 628 304</text>

      <rect class="icon" x="47" y="310" width="15" height="10"/>
      <polyline class="icon" points="47,310 54.5,316 62,310"/>
      <text class="contact" x="75" y="321">lyle_taro@quintmail.example</text>

      <circle class="icon" cx="54.5" cy="347" r="7"/>
      <line class="icon" x1="47.5" y1="347" x2="61.5" y2="347"/>
      <ellipse class="icon" cx="54.5" cy="347" rx="3" ry="7"/>
      <text class="contact" x="75" y="353">www.tarocards.example</text>
    </g>
  </svg>
</div>

</body>
</html>
```